Church needs a street sign design

We're a small church located in Silicon Valley, California. Our website is https://www.hfbmerrow.org/ and our address is 4817 Larkfield Ave, San Jose, California, 95873. You can look up our location on Google Maps to see the sign from Street View. I have uploaded an image of the street sign as well. The marquee, the top section of the sign, and the separating line between them both will be removed. We're seeking a design for a new backlit acrylic insert that will go on the front of the light box and the back of the lightbox. The acrylic sign will fill the entire external frame. In the future, we may build a decorative wood frame around the structural legs, as visualized in one of the uploaded files. The church's brand colors are: #003366 (dark blue), #ff6600 (vibrant orange), #228b22 (forest green). I have also uploaded the church's logo assets. Our primary font is Montserrat and the secondary is Poppins. You can deviate from these colors/fonts if the sign is still coherent with the rest of our branding. Our branding values are mission, truth, passion, and community (please do not put those words on the sign! They are just intended to guide the look of the design). The sign dimensions are 96" by 47.5". Keep in mind that the sign will be backlit on a busy street side. It will also be positioned next to an old-looking church building. We do NOT want a sign that looks traditional, old, or antiquated. Instead, we want a modern-looking sign that pairs well with our old building while helping it look more modern too. We would also like the web address clearly visible on the sign: hfbmerrow.org. If you have any questions, just let me know!

```html
<!DOCTYPE html>
<html lang="en">
<head>
<meta charset="utf-8">
<title>Hope Fellowship Bible Church – Street Sign</title>
<link rel="stylesheet" href="https://fonts.googleapis.com/css2?family=Montserrat:wght@500;600;700&display=swap">
<style>
  :root {
    --brand-blue: #003366;
    --brand-orange: #ff6600;
    --sign-white: #ffffff;
    --backdrop: #b3b3b3;
  }
  html, body {
    margin: 0;
    padding: 0;
    width: 1200px;
    height: 824px;
    overflow: hidden;
    background: var(--backdrop);
  }
  .street-sign {
    position: absolute;
    left: 30px;
    top: 130px;
    width: 1140px;
    height: 564px;
    display: block;
  }
  .sign-face { fill: var(--sign-white); }
  .band { fill: var(--brand-blue); }
  .brand-mark { fill: var(--sign-white); }
  .church-name, .church-subname, .web-address {
    fill: var(--sign-white);
    font-family: "Montserrat", sans-serif;
    font-weight: 500;
  }
  .church-name { font-size: 86px; letter-spacing: 1px; }
  .church-subname { font-size: 30px; letter-spacing: 1px; }
  .web-address { font-size: 80px; font-weight: 700; }
  .heading {
    fill: var(--brand-blue);
    font-family: "Montserrat", sans-serif;
    font-weight: 700;
    font-size: 64px;
  }
  .time-box { fill: var(--brand-orange); }
  .time-text {
    fill: var(--sign-white);
    font-family: "Montserrat", sans-serif;
    font-weight: 600;
    font-size: 48px;
  }
  .address {
    fill: var(--brand-blue);
    font-family: "Montserrat", sans-serif;
    font-weight: 700;
    font-size: 64px;
    letter-spacing: 1px;
  }
  .pin { fill: var(--brand-orange); }
  .pin-hole { fill: var(--sign-white); }
</style>
</head>
<body>
<svg class="street-sign" viewBox="0 0 1945 963" xmlns="http://www.w3.org/2000/svg" aria-label="Hope Fellowship Bible Church street sign">
  <rect class="sign-face" x="0" y="0" width="1945" height="963"/>

  <path class="band band-top" d="M0 0 H1945 V274 L1900 278 1870 272 1840 283 1790 298 1740 292 1700 300 1660 288 1610 282 1560 266 1510 256 1470 262 1420 266 1380 274 1340 256 1300 246 1270 240 1240 258 1200 262 1160 276 1120 286 1080 294 1040 292 1000 288 960 286 930 292 890 290 850 286 810 288 770 282 720 284 680 272 640 268 600 264 560 264 520 270 480 266 440 270 400 268 360 264 320 262 280 264 240 270 200 268 160 262 120 258 80 270 40 274 0 270 Z"/>

  <path class="band band-bottom" d="M0 963 V816 L40 818 80 808 120 800 160 794 200 784 240 780 280 798 320 808 360 806 400 820 440 826 480 828 520 826 560 820 600 828 640 840 680 832 720 826 760 830 800 824 840 826 880 818 920 808 960 804 1000 796 1040 794 1080 798 1120 796 1160 808 1200 814 1240 818 1280 822 1320 826 1360 822 1400 830 1440 826 1480 830 1520 834 1560 826 1600 824 1640 816 1680 820 1720 814 1760 818 1800 812 1840 818 1880 814 1920 816 1945 816 V963 Z"/>

  <g class="church-identity">
    <rect class="brand-mark" x="450" y="88" width="110" height="110"/>
    <text class="church-name" x="596" y="154">HOPE FELLOWSHIP</text>
    <text class="church-subname" x="598" y="193">BIBLE CHURCH</text>
  </g>

  <g class="schedule">
    <text class="heading" x="119" y="407">SUNDAY SERVICE</text>
    <rect class="time-box" x="121" y="424" width="488" height="74"/>
    <text class="time-text" x="136" y="478">10:40 AM - 12:15 PM</text>

    <text class="heading" x="119" y="600">LUNCH PROVIDED</text>
    <rect class="time-box" x="121" y="617" width="488" height="74"/>
    <text class="time-text" x="136" y="671">12:30 PM - 1:30 PM</text>
  </g>

  <g class="location">
    <path class="pin" d="M1010 471 C1038 471 1043 492 1043 504 C1043 512 1040 518 1036 524 L1010 563 L984 524 C980 518 977 512 977 504 C977 492 982 471 1010 471 Z"/>
    <circle class="pin-hole" cx="1010" cy="505" r="15"/>
    <text class="address" x="1099" y="452">4817 Larkfield Ave,</text>
    <text class="address" x="1099" y="537">San Jose,</text>
    <text class="address" x="1099" y="622">California, 95873</text>
  </g>

  <text class="web-address" x="972" y="909" text-anchor="middle">www.hfbmerrow.org</text>
</svg>
</body>
</html>
```